Venture Capital Investment Firm

We are looking to overhaul our existing website (substantially), with only using the same logos (which we can provide).
We are an investment firm that focuses on making loans to late stage technology companies. Our site should ultimately look like other venture capital firms, and look modern and fresh. We have an existing website www.brenvoltfund.com which this will be replacing, although we will be using a lot of the existing written content, and potentially the numbers of pages we will need, we are not wed to anything else. Please feel free to shoot any questions at any time and thank you in advance for your help!
Websites we like as examples:
https://www.tarnwickbay.com/
https://www.morrowlanefinance.com/
Target Market(s)
Potential investors who will invest in our firm, as well as potentially companies that are looking to borrow money from us.
Coding
Colors
Look and feel

```html
<!DOCTYPE html>
<html lang="en">
<head>
<meta charset="utf-8">
<title>Brenvolt — Senior Team</title>
<link href="https://fonts.googleapis.com/css2?family=Questrial&family=Open+Sans:wght@600;700&display=swap" rel="stylesheet">
<style>
:root{
  --navy:#05053a;
  --navy-deep:#03032e;
  --ink:#15154a;
  --text:#3a3a3a;
  --grey-panel:#f0f0f0;
  --footer:#4a4a4a;
  --white:#ffffff;
  --photo-black:#050505;
}
*{margin:0;padding:0;box-sizing:border-box}
html,body{width:741px;height:1200px;overflow:hidden}
body{position:relative;font-family:"Questrial",sans-serif;color:var(--text);background:var(--white)}
.hero{position:absolute;left:0;top:0;width:741px;height:362px;
  background:radial-gradient(ellipse at 30% 70%,#d8d6d4 0%,#b9b6b8 35%,#7f7a8e 70%,#2a2a5a 100%)}
.hero-shade{position:absolute;left:0;top:0;width:741px;height:80px;background:linear-gradient(var(--navy-deep) 0%,rgba(5,5,58,.75) 55%,rgba(5,5,58,0) 100%)}
.brand{position:absolute;left:29px;top:12px;display:flex;align-items:center;gap:8px;color:var(--white)}
.brand-mark{width:22px;height:22px;border-radius:50%;background:var(--white)}
.brand-name{font-family:"Questrial",sans-serif;font-size:17px;letter-spacing:.5px;line-height:1}
.nav{position:absolute;top:19px;right:29px;display:flex;align-items:center}
.nav a{font-family:"Questrial",sans-serif;color:var(--white);font-size:7.5px;letter-spacing:.6px;text-decoration:none;margin-left:25px}
.nav a.investors{background:var(--white);color:var(--navy);padding:5px 7px;margin-left:27px}
.title-band{position:absolute;left:128px;top:120px;width:484px;height:30px;background:rgba(255,255,255,.4);
  text-align:center;font-family:"Open Sans",sans-serif;font-weight:700;font-size:19px;line-height:30px;color:var(--white);text-shadow:1px 1px 2px rgba(0,0,0,.6)}
.hero-kicker{position:absolute;left:370px;top:206px;font-family:"Open Sans",sans-serif;font-weight:600;font-size:18px;color:var(--white);text-shadow:1px 1px 2px rgba(0,0,0,.7)}
.hero-lede{position:absolute;right:366px;top:253px;text-align:right;font-family:"Open Sans",sans-serif;font-weight:700;font-size:12.5px;line-height:16.2px;letter-spacing:1.2px;color:var(--white);text-shadow:1px 1px 2px rgba(0,0,0,.8)}
.member{position:absolute;left:0;width:741px}
.member .portrait{position:absolute;top:0;height:100%;background:radial-gradient(ellipse at 50% 55%,#6a6a6a 0%,#2a2a2a 45%,var(--photo-black) 75%)}
.member .bio{position:absolute;top:0}
.name{font-family:"Open Sans",sans-serif;font-weight:600;font-size:10.5px;color:var(--ink);margin-top:8px}
.role{font-size:9.5px;color:#333;margin-top:6px}
.role span{color:var(--ink)}
.bio p{font-size:7.5px;line-height:10.4px;margin-top:10.4px}
.bio .role + p{margin-top:4px}
.m1{top:362px;height:191px}
.m1 .portrait{left:0;width:265px}
.m1 .bio{left:277px;width:437px}
.m2{top:553px;height:192px;background:var(--grey-panel)}
.m2 .portrait{left:473px;width:268px}
.m2 .bio{left:14px;width:448px;text-align:right}
.m3{top:745px;height:190px}
.m3 .portrait{left:0;width:265px}
.m3 .bio{left:277px;width:440px}
.contact{position:absolute;left:0;top:935px;width:741px;height:201px;background:var(--footer);color:var(--white)}
.contact h3{font-family:"Open Sans",sans-serif;font-weight:700;font-size:10px;letter-spacing:.2px}
.contact p{font-size:8px;margin-top:4px;line-height:10.4px}
.col{position:absolute;top:30px}
.col-a{left:46px}
.col-a .group{margin-bottom:11px}
.col-b{left:265px}
.map{position:absolute;left:427px;top:32px;width:265px;height:137px;background:linear-gradient(90deg,#ecebe6 0%,#e9e8e2 48%,#9fd2f2 55%,#a8d5f1 100%)}
.legal{position:absolute;left:0;top:1136px;width:741px;height:64px;background:var(--navy);color:var(--white)}
.legal .org{position:absolute;left:46px;top:15px;font-size:8px;line-height:11.6px}
.legal nav{position:absolute;left:339px;top:16px;display:flex}
.legal nav a{color:var(--white);text-decoration:none;font-size:7.5px;letter-spacing:.5px;margin-right:23px}
.legal nav a:last-child{margin-right:0}
.legal .disclaimer{position:absolute;left:338px;top:42px;font-size:8px;color:var(--white)}
</style>
</head>
<body>
<header class="hero" role="img" aria-label="Photo of colourful board game pawns standing on a network of connected lines">
  <div class="hero-shade"></div>
</header>
<div class="brand"><span class="brand-mark"></span><span class="brand-name">BRENVOLT</span></div>
<nav class="nav">
  <a href="#">HOME</a><a href="#">STRATEGY</a><a href="#">ABOUT US</a><a href="#">TEAM</a><a href="#">NEWS</a><a href="#">CONTACT</a><a class="investors" href="#">INVESTORS</a>
</nav>
<h1 class="title-band">SENIOR TEAM</h1>
<div class="hero-kicker">Lorem ipsum dolor sit</div>
<div class="hero-lede">Lorem ipsum dolor sit amet,<br>consectetur adipiscing elit.<br>Phasellus orci nulla, convallis<br>eget vulputate ut, pulvinar ut lectus.</div>

<section class="member m1">
  <div class="portrait" role="img" aria-label="Black and white portrait of Elian Marsh in a suit"></div>
  <div class="bio">
    <h2 class="name">Elian Marsh</h2>
    <div class="role"><span>MANAGING PARTNER</span>, Life Sciences, Technology</div>
    <p>Elian Marsh is an industry leader with over $1.2B in structured credit investments since 2004. Elian focuses on origination, underwriting, and portfolio management across sectors at Brenvolt.</p>
    <p>Mr. Marsh was the co-founder of Verdhalcy Credit Partners, a life sciences focused structured credit fund, from 2010-2014. From 2004-2010, Mr. Marsh was Managing Director and Co-Head of the Healthcare Group for the Tollgarth Special Situations Fund at Kestrane Investment Group.</p>
    <p>Prior to joining Kestrane, Mr. Marsh was a member of the investment team at Ravelock Capital where he executed mezzanine debt and leveraged buyouts for middle market companies. Previously, he worked in the Leveraged Finance Group of Halvorsk Brothers, where he structured and underwrote bank loan, high yield bond, and mezzanine debt transactions. Mr. Marsh began his career with Orlenby Capital's Merchant Banking Group. Mr. Marsh earned his joint JD/MBA degrees from Pellbrook Reserve University and a BS in Finance from Vantry State University.</p>
  </div>
</section>

<section class="member m2">
  <div class="bio">
    <h2 class="name">Darin Okafor</h2>
    <div class="role"><span>MANAGING PARTNER</span>, Technology</div>
    <p>Darin Okafor leads technology investment origination and evaluation at Brenvolt. He has over<br>15 years of technology investment and transaction experience.</p>
    <p>Mr. Okafor was a Managing Director and Head of the Strandel Bank Technology Mergers &amp; Acquisitions practice in San Francisco from 2011-2013. Prior to joining Strandel Bank in 2011, Mr. Okafor was a Managing Director with Quenby &amp; Co.'s Technology Banking practice in San Francisco and focused on the Semiconductors and Hardware coverage effort. Previously, Mr. Okafor spent over 7 years with Tessimar Group's Technology M&amp;A Group in Palo Alto and served as a co-head of the Semiconductor Banking Practice.</p>
    <p>As an investment banker, Darin worked globally with large technology firms, emerging companies, venture capitalists, and technology private equity firms, advising on transactions totaling in excess of $75B. Mr. Okafor received an MBA from the Dunmarrow University Graduate School of Business, MSc from the Corwent School of Economics, and a BA from Alderic University.</p>
  </div>
  <div class="portrait" role="img" aria-label="Black and white portrait of Darin Okafor in a suit"></div>
</section>

<section class="member m3">
  <div class="portrait" role="img" aria-label="Black and white portrait of Tobin Harlowe in a suit"></div>
  <div class="bio">
    <h2 class="name">Tobin Harlowe</h2>
    <div class="role"><span>PARTNER</span>, Chief Operating Officer</div>
    <p>Tobin Harlowe serves as the Chief Operating Officer at Brenvolt. He has 20 years of experience in the alternative-investment markets, including private equity fund and firm formation, operations, capital-raising, investor relations, portfolio management and legal transactions.</p>
    <p>Before joining Brenvolt, Mr. Harlowe served as a Managing Director at Argosel &amp; Co. and as a Partner at Linvarra Capital in San Francisco. From 2004 to 2013, he worked as a principal and Managing Director at Fidelmore Partners, where he led private fund placements totaling over $15 billion. Previously, Mr. Harlowe co-managed a group of technology and life-science-focused funds of funds as part of Tessimar Group private equity. He also worked as a corporate finance attorney at Ashvane LLP and Pembrill Lyle LLP, where he represented emerging growth technology companies and investors. Prior to attending law school, he served as Assistant Press Secretary to US Senator Harold James Whitford of New York.</p>
    <p>Mr. Harlowe received a BA from Quarrendon University and a JD from Dunmarrow University.</p>
  </div>
</section>

<footer class="contact">
  <div class="col col-a">
    <div class="group"><h3>GENERAL INQUIRIES:</h3><p>inquiries@brenvoltfund.com</p></div>
    <div class="group"><h3>MEDIA INQUIRIES:</h3><p>media@brenvoltfund.com</p></div>
    <div class="group"><h3>TRANSACTION OPPORTUNITIES</h3><p>invopps@brenvoltfund.com</p></div>
    <div class="group"><h3>CAREERS</h3><p>career@brenvoltfund.com</p></div>
  </div>
  <div class="col col-b">
    <h3>ADDRESS:</h3>
    <p>740 HALDEN STREET #218<br>SAN FRANCISCO, CA 94107</p>
  </div>
  <div class="map" role="img" aria-label="Street map of San Francisco and the bay marking the office location"></div>
</footer>

<div class="legal">
  <div class="org">BRENVOLT, SAN FRANCISCO<br>© 2015 Brenvolt Fund Partners LLC. All Rights Reserved.</div>
  <nav><a href="#">HOME</a><a href="#">STRATEGY</a><a href="#">ABOUT US</a><a href="#">TEAM</a><a href="#">NEWS</a><a href="#">CONTACT</a><a href="#">INVESTORS</a></nav>
  <a class="disclaimer" href="#">Legal Disclaimer</a>
</div>
</body>
</html>
```